Car cleaning and lubrication automotive retail label

Designing a modern, trendy car cleaning and lubrication label for the retail automitive business. the label should be suitable for a retail home and garden product range. We are looking for a label that is realistic and colorful. Greens and blues are what we think would fit best for a eco label. We would like to stand out from other similar product ranges by design, meaning that we are looking for an ultra modern, simple, clean and professional design. We are also looking for a new design for the logo, clean and modern. It should include: The 'KALTOR' logo that can have any color and "Automotive".

Example text for cleaning product (please keep in mind we need a combi cleaning product label that is also suitable for a lubrication label)

The label should have a front and a back:
Front label: Texts and slogans (in dutch):
- Reiniger, ontvetter en polisher
- Bescherming en glans
- Veilig, geconcentreerd en eco friendly
- Milieuvriendelijk
Product name: Stainless Steel Cleaner
Image of car/stainless steel on car
Eco icon
+ Icons explaining the product (cleans stainless steel on car, protection and shine, safe and concentrated, eco friendly, cleaner, degreaser, polisher)

Back label:
Instructions to use
About the product
Remarks
Updates

Target Market(s)

Automotive, car cleaning, car lubrication, car additives

Industry/Entity Type

Automotive

Colors
0692cd
a64599
e33e95
acd037
f04a50
ec1f27
cadf82
33a6d7
33b8a4

Requirements
Must have
• Must have modern colors, cool look, attract customers by an original design

```html
<!DOCTYPE html>
<html lang="nl">
<head>
<meta charset="utf-8">
<title>KALTOR Automotive – Stainless Steel Cleaner label</title>
<link rel="stylesheet" href="https://fonts.googleapis.com/css2?family=Exo+2:ital,wght@0,700;0,800;1,700;1,800&display=swap">
<style>
  :root {
    --page-bg: #ffffff;
    --lime-light: #d8ea1c;
    --lime-deep: #b7d22e;
    --green-curve: #9cc63a;
    --band-black: #1b1b1b;
    --swoosh-grey: #a9acae;
    --sky-blue: #33a6d7;
    --sky-light: #6fc3ea;
    --brand-blue: #0692cd;
    --ink-dark: #2b3200;
    --white: #ffffff;
    --tick-yellow: #e6f21a;
    --eco-dark: #1f2418;
    --photo-grey-1: #d9dcdf;
    --photo-grey-2: #5d6166;
  }
  * { margin: 0; padding: 0; box-sizing: border-box; }
  html, body {
    width: 1200px; height: 1200px; overflow: hidden;
    background: var(--page-bg);
    font-family: "Exo 2", sans-serif;
  }
  .label {
    position: absolute; left: 50px; top: 195px;
    width: 1100px; height: 810px; overflow: hidden;
    box-shadow: 0 6px 24px rgba(0,0,0,0.12);
  }
  .label-shapes { position: absolute; inset: 0; }
  .brand {
    position: absolute; left: 95px; top: 28px;
    font-weight: 800; font-size: 190px; line-height: 1;
    letter-spacing: 4px; color: var(--brand-blue);
  }
  .brand-sub {
    position: absolute; left: 205px; top: 202px;
    font-weight: 700; font-size: 58px; line-height: 1;
    letter-spacing: 2px; color: var(--ink-dark);
  }
  .product-name {
    position: absolute; left: 80px; top: 252px; width: 960px;
    text-align: center; transform: rotate(-7deg);
    font-weight: 800; font-style: italic; font-size: 64px;
    line-height: 1; color: var(--white); letter-spacing: 1px;
  }
  .benefits {
    position: absolute; right: 40px; top: 440px;
    list-style: none; text-align: right;
  }
  .benefits li {
    font-weight: 700; font-style: italic; font-size: 27px;
    line-height: 42px; color: var(--white);
  }
  .benefits svg { width: 26px; height: 24px; margin-left: 8px; vertical-align: -3px; }
</style>
</head>
<body>
  <div class="label">
    <svg class="label-shapes" viewBox="0 0 1100 810" width="1100" height="810">
      <defs>
        <linearGradient id="limeFill" x1="0" y1="0" x2="1" y2="1">
          <stop offset="0" stop-color="var(--lime-light)"/>
          <stop offset="1" stop-color="var(--lime-deep)"/>
        </linearGradient>
        <linearGradient id="photoFill" x1="0" y1="0" x2="1" y2="1">
          <stop offset="0" stop-color="var(--photo-grey-1)"/>
          <stop offset="1" stop-color="var(--photo-grey-2)"/>
        </linearGradient>
        <linearGradient id="skyFill" x1="0" y1="0" x2="0" y2="1">
          <stop offset="0" stop-color="var(--sky-light)"/>
          <stop offset="1" stop-color="var(--sky-blue)"/>
        </linearGradient>
      </defs>
      <rect class="label-bg" width="1100" height="810" fill="url(#limeFill)"/>
      <polygon class="title-band" points="0,318 1100,185 1100,268 0,400" fill="var(--band-black)"/>
      <path class="green-curve" d="M0 600 Q 380 330 1100 330" fill="none" stroke="var(--green-curve)" stroke-width="34"/>
      <path class="car-photo" role="img" aria-label="Photo of a silver car side with alloy wheel and polished trim"
            d="M0 700 Q 360 400 1100 385 L1100 810 L0 810 Z" fill="url(#photoFill)"/>
      <path class="info-panel" d="M560 392 Q 850 382 1100 385 L1100 810 L480 810 Z" fill="url(#skyFill)"/>
      <path class="grey-swoosh" d="M0 680 Q 360 380 1100 370" fill="none" stroke="var(--swoosh-grey)" stroke-width="18"/>
      <circle class="eco-badge" cx="1000" cy="690" r="62" fill="var(--eco-dark)" stroke="var(--green-curve)" stroke-width="6"/>
    </svg>

    <div class="brand">KALTOR</div>
    <div class="brand-sub">AUTOMOTIVE</div>
    <div class="product-name">Stainless Steel Cleaner</div>

    <ul class="benefits">
      <li>Reiniger, ontvetter en polisher<svg viewBox="0 0 26 24"><path d="M3 13 L10 20 L23 3" fill="none" stroke="var(--tick-yellow)" stroke-width="4"/></svg></li>
      <li>Bescherming en glans<svg viewBox="0 0 26 24"><path d="M3 13 L10 20 L23 3" fill="none" stroke="var(--tick-yellow)" stroke-width="4"/></svg></li>
      <li>Veilig, geconcentreerd en eco friendly<svg viewBox="0 0 26 24"><path d="M3 13 L10 20 L23 3" fill="none" stroke="var(--tick-yellow)" stroke-width="4"/></svg></li>
      <li>Milieuvriendelijk<svg viewBox="0 0 26 24"><path d="M3 13 L10 20 L23 3" fill="none" stroke="var(--tick-yellow)" stroke-width="4"/></svg></li>
    </ul>
  </div>
</body>
</html>
```